Postcard Design

I am an attorney in Pittsburgh. Here and across country, companies are sending data with names, address and new criminal charges for people. This has resulted in some people getting 12 or more of these letters. I want to do a postcard because one does not need to open a postcard. I also want to be delicate since there is no sealed envelope. I want to throw in other matters other than criminal so it does not look like the person is necessarily charged with a crime.
At top would be "Law Office of Dorian F. Haslbeck"
Then:
Need an Attorney?
Attorney Dorian F. Haslbeck has 25 Years of Experience
Free Consultation - Affordable Fees - Credit Cards Accepted
-All Criminal Matters
-Most Civil Matters
-DUI / Traffic Citations / License Restoration
412-555-0187
www.lakesidedefenselawyer.example
www.dfhcounsel.example

My CTQ ranking is A+ but I am not sure they give a logo with the rating. I have all my logos at www.lakesidedefenselawyer.example The purpose of the two websites is these are postcards. I want no one to think oh this person is charged with a crime.

Industry/Entity Type

Attorney

```html
<!DOCTYPE html>
<html lang="en">
<head>
<meta charset="utf-8">
<title>Law Office of Dorian F. Haslbeck – Postcard</title>
<link href="https://fonts.googleapis.com/css2?family=Crimson+Text:ital,wght@0,400;0,600;0,700;1,400;1,600;1,700&display=swap" rel="stylesheet">
<style>
  :root{
    --page:#d9d9d9;
    --navy:#0f1a34;
    --navy-mid:#1b2f63;
    --blue:#2b58ad;
    --sky:#5aa6e6;
    --cream:#fbf1d2;
    --red:#b3141b;
    --red-dark:#870b10;
    --orange:#f08a2e;
    --ink:#1b1b1b;
    --white:#ffffff;
    --text-navy:#1c2a55;
  }
  *{margin:0;padding:0;box-sizing:border-box}
  html,body{width:936px;height:1200px;overflow:hidden}
  body{background:var(--page);font-family:"Crimson Text",Georgia,serif;color:var(--ink);position:relative}

  .card{position:absolute;left:48px;width:840px;height:542px;overflow:hidden;box-shadow:0 3px 10px rgba(0,0,0,.25)}
  .card--front{top:36px;background:var(--navy)}
  .card--back{top:620px;background:var(--white);height:544px}

  .front-bg,.front-photo{position:absolute;inset:0}
  .abs{position:absolute}

  /* front: left column */
  .firm-label{left:0;width:290px;top:14px;text-align:center;color:var(--white);font-size:21px}
  .firm-name{left:0;width:290px;top:38px;text-align:center;color:var(--orange);font-size:30px;font-weight:700;line-height:1}
  .firm-rule{left:0;top:84px;width:276px;height:1px;background:#8f9ab8}
  .firm-years{left:0;width:290px;top:88px;text-align:center;color:var(--white);font-size:19px;font-style:italic;font-weight:600}

  .matters{left:24px;top:160px;list-style:none;color:var(--white);font-size:17px;font-weight:600;line-height:22px}
  .matters li{position:relative;padding-left:22px;margin-bottom:3px}
  .matters li::before{content:"✓";position:absolute;left:0;top:0;color:var(--orange);font-weight:700}
  .matters .cont{display:block}

  .badge{border-radius:50%}
  .badge--one{left:38px;top:276px;width:96px;height:96px;background:radial-gradient(circle,#6b2b3a 0 55%,#3a1a29 56% 100%);border:3px solid #b79a6a}
  .badge--two{left:36px;top:412px;width:106px;height:106px;background:radial-gradient(circle,#2c4e8c 0 52%,#c9a24a 53% 100%);border:2px solid #8a6a22}

  /* front: top band */
  .perks{left:340px;top:38px;width:490px;height:50px;display:flex;align-items:center;justify-content:center;color:var(--text-navy);font-size:18px;font-weight:600}
  .perks span{padding:0 10px}
  .perks span+span{border-left:2px solid var(--text-navy)}

  .headline{left:296px;width:510px;top:100px;text-align:center;color:var(--white);font-size:56px;font-style:italic;font-weight:700;line-height:1;text-shadow:0 2px 3px rgba(0,0,0,.35)}

  /* front: right contact */
  .rating{left:772px;top:348px;width:42px;height:70px;background:var(--white);border-radius:4px;display:flex;align-items:flex-end;justify-content:center;padding-bottom:4px}
  .rating .mark{display:block;width:30px;height:30px;background:#1a5ea8;position:absolute;top:8px;left:6px}
  .rating .name{color:#1a5ea8;font-size:13px;font-weight:700}
  .phone-front{right:24px;top:434px;color:var(--orange);font-size:29px;font-weight:600}
  .web-front{right:24px;top:476px;color:var(--white);font-size:16px;font-weight:700;text-align:right;line-height:21px}

  /* back */
  .back-banner{left:0;top:22px;width:440px;height:50px}
  .back-banner-text{left:28px;top:26px;color:var(--white);font-size:22px;font-style:italic;font-weight:600}

  .thumb{left:28px;width:76px;height:84px;border:2px solid #2a5fb0;overflow:hidden}
  .thumb .fill{position:absolute;inset:0}
  .thumb .cap{position:absolute;left:0;right:0;bottom:0;height:18px;background:var(--navy);color:var(--white);font-size:10px;font-weight:700;text-align:center;line-height:18px}
  .thumb--dui{top:96px}
  .thumb--dui .fill{background:linear-gradient(160deg,#3a5fa8,#c9c4c2 55%,#8b2d2a)}
  .thumb--injury{top:191px}
  .thumb--injury .fill{background:linear-gradient(160deg,#6d7e92,#c9ced6 50%,#d56a2a)}
  .thumb--defense{top:286px}
  .thumb--defense .fill{background:linear-gradient(160deg,#d9c7a2,#a8793f 55%,#5b3a1c)}

  .bio{left:127px;top:92px;width:312px;font-size:14.2px;line-height:18.6px;color:var(--ink)}
  .cta{left:127px;top:356px;font-size:20px;font-weight:700;color:var(--ink)}
  .phone-back{left:127px;top:382px;font-size:33px;color:var(--orange)}

  .perks-list{left:108px;top:444px;list-style:none;font-size:15.5px;font-weight:600;line-height:25px}
  .perks-list li{position:relative;padding-left:22px}
  .perks-list li::before{content:"✓";position:absolute;left:0;color:var(--orange);font-weight:700;font-size:18px}

  .address{left:478px;top:46px;color:var(--ink)}
  .address .label{font-size:15px}
  .address .name{font-size:21px;font-weight:600;line-height:1;margin-bottom:12px}
  .address p{font-size:12.5px;line-height:16.5px}
  .address .gap{margin-top:12px}
</style>
</head>
<body>

<section class="card card--front">
  <svg class="front-bg" width="840" height="542" viewBox="0 0 840 542">
    <defs>
      <linearGradient id="frontBase" x1="0" y1="0" x2="1" y2="1">
        <stop offset="0" stop-color="#0d1730"/>
        <stop offset=".45" stop-color="#1b2f63"/>
        <stop offset="1" stop-color="#2b58ad"/>
      </linearGradient>
      <linearGradient id="rightPanel" x1="0" y1="0" x2="0" y2="1">
        <stop offset="0" stop-color="#2f63bd"/>
        <stop offset="1" stop-color="#14274f"/>
      </linearGradient>
      <linearGradient id="redBand" x1="0" y1="0" x2="0" y2="1">
        <stop offset="0" stop-color="#c4161e"/>
        <stop offset="1" stop-color="#870b10"/>
      </linearGradient>
      <linearGradient id="creamBand" x1="0" y1="0" x2="0" y2="1">
        <stop offset="0" stop-color="#fff8e2"/>
        <stop offset="1" stop-color="#f5e2b0"/>
      </linearGradient>
    </defs>
    <rect width="840" height="542" fill="url(#frontBase)"/>
    <polygon points="624,198 840,198 840,542 516,542" fill="url(#rightPanel)"/>
    <polygon points="620,198 640,198 532,542 512,542" fill="#7fb3e8" opacity=".55"/>
    <polygon points="400,0 840,0 840,36 384,36" fill="#5aa6e6"/>
    <polygon points="796,0 840,0 840,36 786,36" fill="#2b58ad"/>
    <polygon points="330,36 840,36 840,90 308,90" fill="url(#creamBand)"/>
    <polygon points="300,90 840,90 840,198 262,198" fill="url(#redBand)"/>
  </svg>
  <svg class="front-photo" width="840" height="542" viewBox="0 0 840 542" role="img" aria-label="Photo of a police officer in a patrol car writing a traffic citation">
    <defs>
      <linearGradient id="photoTone" x1="0" y1="0" x2="1" y2="1">
        <stop offset="0" stop-color="#5d7fa6"/>
        <stop offset=".5" stop-color="#233457"/>
        <stop offset="1" stop-color="#141c30"/>
      </linearGradient>
    </defs>
    <polygon points="210,198 620,198 512,542 132,542" fill="url(#photoTone)"/>
  </svg>

  <p class="abs firm-label">Law Office of</p>
  <p class="abs firm-name">Dorian F. Haslbeck</p>
  <div class="abs firm-rule"></div>
  <p class="abs firm-years">25 years of experience</p>

  <ul class="abs matters">
    <li>All Criminal Matters</li>
    <li>Most Civil Matters</li>
    <li>DUI / Traffic Citations /<span class="cont">License Restoration</span></li>
  </ul>

  <div class="abs badge badge--one" role="img" aria-label="Lawyer ranking seal"></div>
  <div class="abs badge badge--two" role="img" aria-label="Trial lawyer association seal"></div>

  <div class="abs perks"><span>Free Consultation</span><span>Affordable Fees</span><span>Credit Cards Accepted</span></div>
  <h1 class="abs headline">Need an Attorney?</h1>

  <div class="abs rating"><span class="mark"></span><span class="name">CTQ</span></div>
  <p class="abs phone-front">(412) 555-0187</p>
  <p class="abs web-front">www.lakesidedefenselawyer.example<br>www.dfhcounsel.example</p>
</section>

<section class="card card--back">
  <svg class="abs back-banner" width="440" height="50" viewBox="0 0 440 50">
    <defs>
      <linearGradient id="backRed" x1="0" y1="0" x2="0" y2="1">
        <stop offset="0" stop-color="#c4161e"/>
        <stop offset="1" stop-color="#870b10"/>
      </linearGradient>
    </defs>
    <polygon points="0,0 440,0 420,50 0,50" fill="url(#backRed)"/>
  </svg>
  <p class="abs back-banner-text">Let him put his experience to work for you.</p>

  <div class="abs thumb thumb--dui"><div class="fill" role="img" aria-label="Photo of a driver being stopped by police"></div><span class="cap">DUI Defense</span></div>
  <div class="abs thumb thumb--injury"><div class="fill" role="img" aria-label="Photo of a damaged car after a collision"></div><span class="cap">Personal Injury</span></div>
  <div class="abs thumb thumb--defense"><div class="fill" role="img" aria-label="Photo of scales of justice and a gavel"></div><span class="cap">Criminal Defense</span></div>

  <p class="abs bio">Pittsburgh Criminal Defense Attorney Dorian F. Haslbeck has over 24 years of experience representing clients charged with crimes including Murder, Drug Felonies (state and Federal Court), Assault, Sexual Offenses, Burglary and DUI. He is recognized as a TOP 100 Lawyer by The Trial Advocates Guild, has been rated a perfect 10 by Rately and has taught continuing legal education classes to other attorneys. If you are charged with a crime and need an experienced defense attorney contact the Law Office of Dorian F. Haslbeck today. Let him put his experience to work for you.</p>

  <p class="abs cta">Call today for a free consultation at</p>
  <p class="abs phone-back">(412) 555-0187.</p>

  <ul class="abs perks-list">
    <li>Free Consultation</li>
    <li>Affordable Fees</li>
    <li>Credit Cards Accepted</li>
  </ul>

  <address class="abs address" style="font-style:normal">
    <p class="label">Law Office of</p>
    <p class="name">Dorian F. Haslbeck</p>
    <p>1150 Harbor Court Building</p>
    <p>305 Lakeview Avenue</p>
    <p>Pittsburgh, PA 15219</p>
    <p class="gap">TEL: 412-555-0187 or 412-555-0142</p>
    <p>FAX: 412-555-0199</p>
    <p class="gap">www.lakesidedefenselawyer.example</p>
    <p>www.dfhcounsel.example</p>
  </address>
</section>

</body>
</html>
```